Trip-Hop Instrumental Album from Producer Ravi Lund needs a Front/Back Cover Design!

I need a CD cover design for the front and back of an instrumental hip-hop album that I've composed (so that I could print CD's or vinyls if I want to). The title of the album is Halcyon, and the artist name is Ravi Lund. I'd like just the name of the album and the artist name on the front, and then the tracklisting on the back. The album is a collection of trippy hip-hop instrumentals, and the tracklisting is as follows:

Quiet over Lakeshore
Glass Hour
Dust and Hum
Waltz for the Grey Coast
Tin Lane
Pendulum
Let It Fade
Origami

Here's a couple of the tracks that I put up, just to help you catch the vibe, if that helps.
https://tunevault.example/ravilund/netsuke-instrumental
https://tunevault.example/ravilund/numb-in-toronto-instrumental
https://tunevault.example/ravilund/poverty-and-bass-instrumental-1

Here's a few examples of some cover art that caught my eye. I don't want a carbon copy of these covers, but I absolutely love the atmosphere and the vibe that they create - smoky, etheral, trippy/glitchy yet weirdly beautiful, that kind of stuff generally. Just a general idea of the mood I'm looking for coverwise. I've also attached a couple photos of myself (one from the front, one from the side) so that if you decide you wanted to work a drawing of that into the front cover or the back cover you have that option if that's the vibe you're feeling. I'm trying to give you as much information as possible so that this process is easy, I hope the info I've given you is adequate. Overall I'm just looking for a cover/rear cover that will best accompany the music I've made, and I trust you will be able to help me achieve this.

Some examples of covers that I really like the atmosphere of (they're all pretty different so it might be worth taking a look at them):
Example 1: https://www.clipstream.example/watch?v=7hTrwQZmLpX
Example 2: https://www.clipstream.example/watch?v=kBv-eoW4npq&list=PL8qTRN_2xmHd4sjwuLpKOAr7NcYPeeXwa&index=105
Example 3: https://www.clipstream.example/watch?v=9-hTdPWsYmu&index=22&list=FLBq_wkX4_cxZ7Rt2qjdHVLk
Example 4: https://www.clipstream.example/watch?v=ezK4CLNw5tb

If you need any more information, please contact me at ravilund@postwell.example and I'll be happy to give you any more information you'd like. Thank you very much.

Requirements
Must have
• Lo-fi, retro feel, doesn't look like a word-art collage. Preferably the album name/artist name in smallish writing (some jagged font) so that the main focus is whatever the main image on the cover is. Also I'd prefer it if there were just one image on the front cover, which takes up the whole cover, and then the artist name/album title on the front but not very large so that the main focus is whatever the image is. Again, lo-fi, dark, atmospheric, trippy is the way to go. Please no images of people. If you want to see some examples of covers that I liked check the project description because there are links in there to some covers that I liked.

```html
<!DOCTYPE html>
<html lang="en">
<head>
<meta charset="utf-8">
<title>Halcyon — Ravi Lund — Back Cover</title>
<link rel="stylesheet" href="https://fonts.googleapis.com/css2?family=Josefin+Sans:ital,wght@1,300&display=swap">
<style>
  :root {
    --ink: #000000;
    --amber: #f7941d;
  }
  html, body {
    margin: 0;
    padding: 0;
    width: 1200px;
    height: 1200px;
    overflow: hidden;
    background: var(--ink);
  }
  .back-cover {
    position: relative;
    width: 1200px;
    height: 1200px;
    background: var(--ink);
  }
  .frame-outer {
    position: absolute;
    left: 216px;
    top: 123px;
    width: 768px;
    height: 954px;
    box-sizing: border-box;
    border: 21px solid var(--amber);
  }
  .frame-inner {
    position: absolute;
    left: 277px;
    top: 197px;
    width: 646px;
    height: 806px;
    box-sizing: border-box;
    border: 3px solid var(--amber);
  }
  .tracklist {
    position: absolute;
    left: 277px;
    top: 246px;
    width: 646px;
    margin: 0;
    padding: 0;
    list-style: none;
    text-align: center;
    font-family: "Josefin Sans", sans-serif;
    font-style: italic;
    font-weight: 300;
    font-size: 37px;
    line-height: 88.6px;
    color: var(--amber);
  }
</style>
</head>
<body>
  <main class="back-cover">
    <div class="frame-outer"></div>
    <div class="frame-inner"></div>
    <ol class="tracklist">
      <li class="track">Quiet over Lakeshore</li>
      <li class="track">Glass Hour</li>
      <li class="track">Dust and Hum</li>
      <li class="track">Waltz for the Grey Coast</li>
      <li class="track">Tin Lane</li>
      <li class="track">Pendulum</li>
      <li class="track">Let It Fade</li>
      <li class="track">Origami</li>
    </ol>
  </main>
</body>
</html>
```